Create for us a Shop-Stopper Business Card

We need a standout, first class business card to go along with our new brand strategy. Sleek, Contemporary and fresh.

Colors and theme must sync with our websitewww.pelvorpower.co.uk

We want a business card that has a global brand appeal. TKR Energy is a small UK renewable company that specialises in energy projects in Africa. We want a business card that has the following characteristics: Very short, precise, global, stand out, NOT TOO LOUD but contemporary. The company's colour themes are White, Grey with a hint of green.

Target Market(s)

Business exec, high net worth individuals, investors, commercial leaders, suppliers, government officials

Industry/Entity Type

Solar Energy

Contact Information for Business Card

Logo, Name, Title, Address, web address, email,

Requirements
Must have
• Logo must be sharp
Nice to have
• Adapt fonts from the logo. The large circular side of the logo at the back in a very refreshing way
Should not have
• No solar panel shapes or image.Very little black. If possible avoid black. Its not coming out nice. I think !!!

```html
<!DOCTYPE html>
<html lang="en">
<head>
<meta charset="utf-8">
<title>TKR Energy – Business Card</title>
<link href="https://fonts.googleapis.com/css2?family=Open+Sans:wght@300;400;600;700&display=swap" rel="stylesheet">
<style>
  :root {
    --stage-bg: #2f2f2f;
    --green-deep: #0a7a3a;
    --green-mid: #2a9645;
    --green-light: #7ab648;
    --lime: #c6d934;
    --yellow: #f2e43a;
    --white: #ffffff;
    --grey-text: #4a4a4a;
  }
  * { margin: 0; padding: 0; box-sizing: border-box; }
  html, body {
    width: 1200px; height: 900px; overflow: hidden;
    background: var(--stage-bg);
    font-family: "Open Sans", Arial, sans-serif;
  }
  .stage { position: relative; width: 1200px; height: 900px; }

  .card {
    position: absolute; top: 302px;
    width: 513px; height: 295px;
    border-radius: 22px; overflow: hidden;
  }
  .card--front { left: 73px; background: var(--green-deep); }
  .card--back { left: 616px; background: var(--white); }

  /* front */
  .front-artwork {
    position: absolute; inset: 0;
    background:
      radial-gradient(ellipse 45% 70% at 48% 45%, var(--green-light) 0%, rgba(122,182,72,0) 100%),
      radial-gradient(ellipse 30% 60% at 78% 75%, rgba(242,228,58,0.55) 0%, rgba(242,228,58,0) 100%),
      radial-gradient(ellipse 30% 60% at 20% 80%, rgba(198,217,52,0.5) 0%, rgba(198,217,52,0) 100%),
      linear-gradient(135deg, var(--green-mid), var(--green-deep));
  }
  .front-web {
    position: absolute; left: 165px; top: 137px;
    color: var(--white); font-size: 14px; font-weight: 400; letter-spacing: 0.2px;
  }
  .front-web strong { font-weight: 700; }

  /* back */
  .brand {
    position: absolute; left: 34px; top: 44px;
    display: flex; align-items: center; gap: 8px;
  }
  .brand-dot {
    width: 44px; height: 44px; border-radius: 50%;
    background: var(--green-mid);
  }
  .brand-name {
    color: var(--grey-text); font-size: 27px; font-weight: 600; letter-spacing: 0.5px;
  }
  .contact-band {
    position: absolute; left: 0; right: 0; top: 180px; bottom: 0;
    background: linear-gradient(90deg, var(--green-deep) 0%, var(--green-mid) 45%, var(--green-light) 100%);
    border-top: 3px solid var(--lime);
  }
  .person {
    position: absolute; left: 48px; top: 20px; color: var(--white);
  }
  .person-name { font-size: 15px; font-weight: 700; line-height: 20px; }
  .person-title, .person-email { font-size: 13.5px; font-weight: 300; line-height: 20px; }
  .office {
    position: absolute; left: 342px; top: 28px;
    border-left: 1px solid var(--white);
    padding-left: 10px; color: var(--white);
    font-size: 11.5px; font-weight: 300; line-height: 14.5px;
  }
  .office-name { font-weight: 700; }
</style>
</head>
<body>
<main class="stage">
  <section class="card card--front">
    <div class="front-artwork" role="img" aria-label="Large brand symbol artwork: leaf with curving green and yellow arrows"></div>
    <p class="front-web">www.<strong>pelvorpower</strong>.co.uk</p>
  </section>

  <section class="card card--back">
    <div class="brand">
      <span class="brand-dot"></span>
      <span class="brand-name">TKR ENERGY</span>
    </div>
    <div class="contact-band">
      <div class="person">
        <p class="person-name">Daniel Morrow</p>
        <p class="person-title">managing director</p>
        <p class="person-email">d.morrow@pelvorpower.co.uk</p>
      </div>
      <address class="office" style="font-style:normal">
        <p class="office-name">TKR Energy</p>
        <p>48 Harbour Lane</p>
        <p>Westbridge, Kent</p>
        <p>KT4 9RL</p>
      </address>
    </div>
  </section>
</main>
</body>
</html>
```